" A empresa ainda é nova e irá trabalhar com projetos e obras para terceiros, estou querendo atuar principalmente em condomínio fechado na construções de casas. "

```html
<!DOCTYPE html>
<html lang="pt-BR">
<head>
<meta charset="utf-8">
<title>ARCO Projetos e Construções — Blocos de notas</title>
<link href="https://fonts.googleapis.com/css2?family=Montserrat:wght@400;600;700&display=swap" rel="stylesheet">
<style>
  :root {
    --backdrop: #eceeef;
    --paper: #ffffff;
    --navy: #1b2f45;
    --navy-deep: #152638;
    --teal: #2aa3c6;
    --wire: #6c7075;
    --muted: #9aa3ab;
  }
  * { box-sizing: border-box; margin: 0; padding: 0; }
  html, body { width: 1200px; height: 1200px; overflow: hidden; }
  body {
    background: var(--backdrop);
    font-family: "Montserrat", Arial, sans-serif;
    position: relative;
  }
  .notepad {
    position: absolute;
    background: var(--paper);
    box-shadow: 0 6px 18px rgba(0,0,0,0.12);
  }
  .notepad__spiral {
    position: absolute;
    left: 0; right: 0; top: -22px;
    height: 36px;
  }
  .notepad--cover { left: 163px; top: 413px; width: 305px; height: 440px; }
  .notepad--sheet { left: 463px; top: 360px; width: 270px; height: 420px; }
  .notepad--dark  { left: 737px; top: 403px; width: 300px; height: 450px; background: var(--navy); }

  .brand { position: absolute; left: 0; right: 0; text-align: center; }
  .brand__name {
    font-weight: 700;
    color: var(--navy);
    letter-spacing: 0.06em;
    line-height: 1;
  }
  .brand__tagline {
    font-weight: 600;
    color: var(--teal);
    text-transform: uppercase;
    letter-spacing: 0.14em;
    margin-top: 6px;
  }
  .brand__mark {
    display: block;
    margin: 0 auto 10px;
    background: var(--teal);
  }

  .notepad--cover .brand { top: 150px; }
  .notepad--cover .brand__mark { width: 34px; height: 34px; }
  .notepad--cover .brand__name { font-size: 52px; }
  .notepad--cover .brand__tagline { font-size: 9.5px; }

  .notepad--sheet .brand { top: 32px; }
  .notepad--sheet .brand__mark { width: 18px; height: 18px; margin-bottom: 5px; }
  .notepad--sheet .brand__name { font-size: 24px; }
  .notepad--sheet .brand__tagline { font-size: 5px; margin-top: 3px; }

  .notepad--dark .brand { top: 200px; }
  .notepad--dark .brand__mark { width: 26px; height: 26px; }
  .notepad--dark .brand__name { font-size: 42px; color: #ffffff; }
  .notepad--dark .brand__tagline { font-size: 7.5px; }

  .cover-footer {
    position: absolute; left: 0; right: 0; bottom: 0;
    height: 24px; background: var(--navy);
    border-bottom: 6px solid var(--teal);
  }
  .contact-bar {
    position: absolute; left: 0; right: 0; bottom: 0;
    height: 28px; background: var(--navy-deep);
    display: flex; justify-content: space-around; align-items: center;
    padding: 0 14px;
    font-size: 7px; color: #d9e2ea;
  }
  .contact-bar span::after {
    content: ""; display: inline-block; width: 5px; height: 5px;
    border-radius: 50%; background: var(--teal); margin-left: 4px; vertical-align: middle;
  }
</style>
</head>
<body>

  <section class="notepad notepad--cover">
    <svg class="notepad__spiral" viewBox="0 0 305 36" preserveAspectRatio="none" aria-hidden="true">
      <g fill="none" stroke="var(--wire)" stroke-width="2">
        <path d="M12 30 v-22 M22 30 v-22 M32 30 v-22 M42 30 v-22 M52 30 v-22 M62 30 v-22 M72 30 v-22 M82 30 v-22 M92 30 v-22 M102 30 v-22 M112 30 v-22 M122 30 v-22 M132 30 v-22 M142 30 v-22 M152 30 v-22 M162 30 v-22 M172 30 v-22 M182 30 v-22 M192 30 v-22 M202 30 v-22 M212 30 v-22 M222 30 v-22 M232 30 v-22 M242 30 v-22 M252 30 v-22 M262 30 v-22 M272 30 v-22 M282 30 v-22 M292 30 v-22"/>
      </g>
    </svg>
    <div class="brand">
      <span class="brand__mark"></span>
      <div class="brand__name">ARCO</div>
      <div class="brand__tagline">Projetos e Construções</div>
    </div>
    <div class="cover-footer"></div>
  </section>

  <section class="notepad notepad--sheet">
    <svg class="notepad__spiral" viewBox="0 0 270 36" preserveAspectRatio="none" aria-hidden="true">
      <g fill="none" stroke="var(--wire)" stroke-width="2">
        <path d="M12 30 v-22 M22 30 v-22 M32 30 v-22 M42 30 v-22 M52 30 v-22 M62 30 v-22 M72 30 v-22 M82 30 v-22 M92 30 v-22 M102 30 v-22 M112 30 v-22 M122 30 v-22 M132 30 v-22 M142 30 v-22 M152 30 v-22 M162 30 v-22 M172 30 v-22 M182 30 v-22 M192 30 v-22 M202 30 v-22 M212 30 v-22 M222 30 v-22 M232 30 v-22 M242 30 v-22 M252 30 v-22"/>
      </g>
    </svg>
    <div class="brand">
      <span class="brand__mark"></span>
      <div class="brand__name">ARCO</div>
      <div class="brand__tagline">Projetos e Construções</div>
    </div>
  </section>

  <section class="notepad notepad--dark">
    <svg class="notepad__spiral" viewBox="0 0 300 36" preserveAspectRatio="none" aria-hidden="true">
      <g fill="none" stroke="var(--wire)" stroke-width="2">
        <path d="M14 30 v-22 M26 30 v-22 M38 30 v-22 M50 30 v-22 M62 30 v-22 M74 30 v-22 M86 30 v-22 M98 30 v-22 M110 30 v-22 M122 30 v-22 M134 30 v-22 M146 30 v-22 M158 30 v-22 M170 30 v-22 M182 30 v-22 M194 30 v-22 M206 30 v-22 M218 30 v-22 M230 30 v-22 M242 30 v-22 M254 30 v-22 M266 30 v-22 M278 30 v-22 M290 30 v-22"/>
      </g>
    </svg>
    <div class="brand">
      <span class="brand__mark"></span>
      <div class="brand__name">ARCO</div>
      <div class="brand__tagline">Projetos e Construções</div>
    </div>
    <div class="contact-bar">
      <span>Rua Aurora, 120 Centro</span>
      <span>contato@arcoobras.com</span>
      <span>(11) 4000-1234</span>
    </div>
  </section>

</body>
</html>
```